The Velvet Heron Business Card

Looking for new business cards for our Directors and Manager
I have attached what they are currently, they are also gold foiled where you see gold sections. We do want them to be quite special and exciting being a show venue.
Please use Lanternshowhouse logo for Dean Morcup and Kaye Lindahl, please use Velvet Heron Marqueeland for Jed Quall and Martin Gabe

https://files.examplevault.net/f/7QpLwX2mRtz9KbVnYc4HsD8gJe3UaFo?mode=view_link

I need 3 different versions for Directors and Managers.
Card One:
Dean Morcup
Director of The Velvet Heron Lanternshowhouse
0492 647 258
dean@quellary.com.au
velvetheronshows.com

Card Two:
Martin Gabe
Director of The Velvet Heron Marqueeland
0463 921 574
martin@vhmq.com.au
velvetheronshows.com

Card Three:
Jed Quall
Venue Manager of The Velvet Heron Marqueeland
0447 286 190
qldoperations@vhmq.com.au
velvetheronshows.com

Card Four:

Kaye Lindahl
0428 364 917
kaye@skyhoopers.com.au
velvetheronshows.com

Logo:
https://files.examplevault.net/f/9HtRwq4ZmNb2XcLpVe6YdKs8FjA3uTg

Colour Scheme: Hot Pink and Baby Pink
Gold Accents

We want something different but as inspiration, I have attached the current card. The gold part was foiled. Standard business card sizes.

```html
<!DOCTYPE html>
<html lang="en">
<head>
<meta charset="utf-8">
<title>The Velvet Heron Business Card</title>
<link rel="stylesheet" href="https://fonts.googleapis.com/css2?family=Bebas+Neue&family=Oswald:wght@400;500&display=swap">
<style>
  :root {
    --hot-pink: #e5339a;
    --baby-pink: #f7b6dc;
    --glow-pink: rgba(229, 51, 154, 0.42);
    --gold: #d9a441;
    --ink: #1c1c1f;
    --card-black: #050608;
    --card-white: #ffffff;
    --backdrop: #efefef;
  }
  * { box-sizing: border-box; margin: 0; padding: 0; }
  html, body {
    width: 1046px; height: 1200px; overflow: hidden;
    background: var(--backdrop);
  }
  .canvas { position: relative; width: 1046px; height: 1200px; }

  .card {
    position: absolute; left: 126px; width: 794px; height: 454px;
    box-shadow: 0 18px 40px rgba(0,0,0,0.18);
    overflow: hidden;
  }
  .card--front { top: 102px; background: var(--card-black); }
  .card--back  { top: 645px; background: var(--card-white); }

  .mark-glow {
    position: absolute; border-radius: 50%;
  }
  .card--front .mark-glow {
    left: 177px; top: 40px; width: 440px; height: 340px;
    background: radial-gradient(closest-side, var(--glow-pink), rgba(229,51,154,0.12) 60%, transparent);
  }
  .card--back .mark-glow {
    left: 400px; top: 110px; width: 370px; height: 230px;
    background: radial-gradient(closest-side, rgba(247,182,220,0.75), rgba(247,182,220,0.25) 60%, transparent);
  }

  .venue-mark {
    position: absolute; display: flex; align-items: center;
  }
  .venue-mark__dot {
    flex: none; border-radius: 50%; background: var(--hot-pink);
  }
  .venue-mark__name {
    font-family: "Bebas Neue", sans-serif; font-weight: 400;
    color: var(--gold); line-height: 0.92; letter-spacing: 1px;
  }
  .card--front .venue-mark { left: 0; right: 0; top: 150px; justify-content: center; gap: 24px; }
  .card--front .venue-mark__dot { width: 112px; height: 112px; }
  .card--front .venue-mark__name { font-size: 76px; }

  .card--back .venue-mark { left: 424px; top: 180px; gap: 16px; }
  .card--back .venue-mark__dot { width: 60px; height: 60px; }
  .card--back .venue-mark__name { font-size: 42px; }

  .contact { position: absolute; left: 64px; top: 114px; }
  .contact__name {
    font-family: "Bebas Neue", sans-serif; font-size: 74px; line-height: 1;
    color: var(--hot-pink); letter-spacing: -0.5px;
  }
  .contact__role {
    margin-top: 2px; margin-left: 4px; width: 220px;
    font-family: "Oswald", sans-serif; font-weight: 400; font-size: 18px;
    line-height: 1.25; color: var(--ink); text-transform: uppercase; letter-spacing: -0.2px;
  }
  .contact__list { list-style: none; margin-top: 20px; margin-left: 4px; }
  .contact__item {
    display: flex; align-items: center; gap: 8px; height: 26px;
    font-family: "Oswald", sans-serif; font-weight: 400; font-size: 18px;
    color: var(--ink); letter-spacing: -0.3px;
  }
  .contact__icon { width: 13px; height: 13px; flex: none; fill: var(--hot-pink); }

  .divider {
    position: absolute; left: 381px; top: 131px; width: 1px; height: 204px;
    background: var(--hot-pink);
  }
</style>
</head>
<body>
<main class="canvas">
  <section class="card card--front" aria-label="Card front">
    <span class="mark-glow" role="img" aria-label="Soft pink neon glow behind the venue name"></span>
    <div class="venue-mark">
      <span class="venue-mark__dot"></span>
      <span class="venue-mark__name">The Velvet Heron<br>Lanternclub</span>
    </div>
  </section>

  <section class="card card--back" aria-label="Card back">
    <div class="contact">
      <h1 class="contact__name">Jed Quall</h1>
      <p class="contact__role">Venue Manager of The Velvet Heron Marqueeland</p>
      <ul class="contact__list">
        <li class="contact__item">
          <svg class="contact__icon" viewBox="0 0 24 24" aria-hidden="true"><path d="M6.6 10.8a15.1 15.1 0 0 0 6.6 6.6l2.2-2.2c.3-.3.7-.4 1-.2 1.1.4 2.3.6 3.6.6.6 0 1 .4 1 1V20c0 .6-.4 1-1 1A17 17 0 0 1 3 4c0-.6.4-1 1-1h3.5c.6 0 1 .4 1 1 0 1.3.2 2.5.6 3.6.1.3 0 .7-.2 1z"/></svg>
          0447 286 190
        </li>
        <li class="contact__item">
          <svg class="contact__icon" viewBox="0 0 24 24" aria-hidden="true"><path d="M2 5h20v14H2z"/><path d="M3 6.5 12 12.5 21 6.5" fill="none" stroke="#fff" stroke-width="1.6"/></svg>
          qldoperations@vhmq.com.au
        </li>
        <li class="contact__item">
          <svg class="contact__icon" viewBox="0 0 24 24" aria-hidden="true"><circle cx="12" cy="12" r="10"/><path d="M2 12h20M12 2c3 3 3 17 0 20M12 2c-3 3-3 17 0 20M4 7h16M4 17h16" fill="none" stroke="#fff" stroke-width="1.3"/></svg>
          velvetheronshows.com
        </li>
      </ul>
    </div>
    <span class="divider"></span>
    <span class="mark-glow" role="img" aria-label="Soft baby pink glow behind the venue name"></span>
    <div class="venue-mark">
      <span class="venue-mark__dot"></span>
      <span class="venue-mark__name">The Velvet Heron<br>Lanternclub</span>
    </div>
  </section>
</main>
</body>
</html>
```